Dynamic Website Design For Dynamic Speaker and Business Coach!

Professional Website Design for a for a Professional Business coach, Business trainer, and Speaker.

Note: This is for design only. No coding required. We want to see your ideas for a great website! This will be a FUN design and not boring like others you may work on.

Please let your creative ideas flow. We have given you a ton of info along with videos to help you understand what we are after, however we WANT your creativity to shine through in your designs!

We are a professional company that has run hundreds of crowdsourced projects on multiple platforms. If you participate in this contest (we hope you do) you can expect great video feedback, consistent feedback, and also our guarantee that if we know your website design will not be what we are looking for we will notify you so you don’t waste your time if there is no chance of you winning.

We respect and recognize this is how you make your living and we will not play games. We look forward to an awesome contest and awesome website designs.

Design Brief:

We are looking for a fresh and fun new design for

http://www.brightpath-advisory.net

This individual (Dana Holloway) teaches and trains corporations and businesses in the fields of leadership, sales, communication, business operations etc. Additionally this business teaches and mentors business professionals in a small group level or 1 on 1.

The website needs to convey trust, professionalism, and affluent, while at the same time having some personality!

This business operates on 3 core principles that we would like to see incorporated into the logo if it is a good fit. The 3 principals are:

Focus
Accountability
Results

Here is a video to help explain what we like about the current site and what we don’t like:
http://clipvault.example/t/QwpLmr82kTnb

As you can see the website is geared towards business professionals. Please look over the website to learn what they do. Obviously this is not a good website so we need your help.

We want a website that is professional-looking, has personality and is geared more towards promoting Dana Holloway, the owner of Summit Path Advisory as a Speaker and Business Consultant. The more you can incorporate clean, professional and fun personality elements into the design, the better off you are at winning.

Here are some examples of other sites in their business that have some things we like:

http://velvetcompass.com Please watch video to learn what we like and don’t like:
http://clipvault.example/t/NrtHq7YpLwc

http://tallpinegrowth.com Please watch video to learn what we like and don’t like:
http://clipvault.example/t/J8vDkrWa

http://www.marthaquince.com Please watch video to learn what we like and don’t like:
http://clipvault.example/t/Pz3mx9Rb2Kq

http://www.vantix7.com Please watch video to learn what we like and don’t like:
http://clipvault.example/t/7Gwe4sNhydv

NOTE: We do not want to copy anything outright. We want to learn, model and take their ideas and make them better. We also want to be flexible and take what we like along with your creativity to make an amazing design.

Here is what we are looking for in more specific terms:

Colors: We like the darker blue (not the light blue like the site) and also a burnt orange. I’ve attached her Logo so you can get an idea and feel for the colors.

When looking at colors please know that the current site and look is NOT what we are going for. We are going for a clean and professional look but also a look that is BOLD, FUN, and Vibrant (hence the colors).

Menu: Horizontal. We like bold and easy to read menu items. Don’t make it small and cluttered.

Site Structure: Clean and easy to navigate. We have a lot of content to display so we need a clean structure that breaks up the text and content areas.
Images: Please pull images from the current site. We can always replace the images of course, but if you show them “their own stuff” in the new design you will be closer to winning because it will feel more like “them”

Look and Feel: Professional. Fun. High-End. Business-like. This website needs to convey that Dana Holloway and Summit Path Advisory are professional. That Dana Holloway is a sought-after Speaker and Business Consultant who knows what she is talking about; can be serious when she needs to be, but also likes to have fun with her clients. This site must convey that!

Content Areas: It is a safe bet that if it is on the current site we need it on the new site. So don’t drop anything as it makes it hard to “cut content”.

What we don't want: We do not want clutter, boring, or templates or themes. We don’t want too cartoony, too cute, or too fancy… Be creative!

Out of respect to professional designers who really are working hard to win if you do not follow this brief, you submit worn out themes, templates, or boring designs you will be eliminated. We are offering great prize money for this so we expect great visual designs.
Updates

Project Deadline Extended
Reason: Our client is out of town, and waiting to hear feedback from them. So, in the meantime, we wanted to keep the project going to see what else you designers can come up with. As soon as we hear back from our client, we will pass along the info. Thanks!

Target Market(s)

Target Audience is entrepreneurs and business professionals alike. This is all business to business stuff.

This person teaches and trains startups and billion dollar companies. The common thread is that they are all businesses and companies who need help in various areas including sales, communication, business operations, etc.

Industry/Entity Type

Business

Font styles to use
Sans Serif

Requirements
Must have
• Brief is very detailed. Please review
Nice to have
Should not have

```html
<!DOCTYPE html>
<html lang="en">
<head>
<meta charset="utf-8">
<title>Summit Path Advisory — Albuquerque Business Coaching and Consulting</title>
<link rel="stylesheet" href="https://fonts.googleapis.com/css2?family=Open+Sans:wght@400;600;700&family=Montserrat:wght@700&display=swap">
<style>
:root{
  --orange:#f36f21;
  --orange-deep:#e35e12;
  --nav:#e8823a;
  --navy:#1c2a55;
  --navy-deep:#121a36;
  --sky:#c9d8e6;
  --text:#6b6b6b;
  --heading:#444;
  --band:#ececec;
  --white:#fff;
  --footer:#272727;
  --footer-base:#1d1d1d;
  --footer-text:#9b9b9b;
  --track:#e4e4e4;
  --btn:#8c8c8c;
  --social:#3e67b1;
}
*{box-sizing:border-box;margin:0;padding:0}
html,body{width:1200px;height:1000px;overflow:hidden;background:var(--white)}
body{position:relative;font-family:"Open Sans",Arial,sans-serif;color:var(--text)}
.abs{position:absolute}
p{font-size:8px;line-height:10.5px}

/* header */
.topline{left:0;top:0;width:1200px;height:3px;background:var(--orange)}
.brand{left:105px;top:6px;display:flex;align-items:center;gap:6px}
.brand-dot{width:22px;height:22px;border-radius:50%;background:var(--orange)}
.brand-name{font-size:16px;font-weight:700;color:var(--orange);line-height:1}
.social-top{left:958px;top:3px;display:flex;gap:18px}
.social-top span{width:14px;height:14px;border-radius:50%;background:var(--social)}
.social-top span:nth-child(4){background:var(--orange)}
.search{left:922px;top:22px;width:158px;height:11px;border:1px solid #f4b48a;background:var(--white)}
.search svg{position:absolute;right:6px;top:0}

/* nav */
.nav{left:0;top:36px;width:1200px;height:17px;background:var(--nav);display:flex;justify-content:space-between;padding:0 138px 0 123px;align-items:center}
.nav a{color:var(--white);font-size:8px;text-decoration:none}

/* hero */
.hero{left:0;top:53px;width:1200px;height:147px;
  background:
    radial-gradient(ellipse 150px 120px at 295px 110px,#e9c98c 0%,#d9b57c 35%,rgba(230,215,190,0) 100%),
    radial-gradient(ellipse 140px 60px at 295px 170px,#2b2628 0%,rgba(43,38,40,.6) 50%,rgba(43,38,40,0) 100%),
    linear-gradient(90deg,#f3efe8 0%,#f1e6d2 40%,#f6efe0 58%,var(--sky) 80%,#e9eef2 100%)}
.hero-banner{left:665px;top:160px;width:535px;height:40px}
.hero-title{left:728px;top:164px;font-family:"Montserrat",Arial,sans-serif;font-weight:700;font-size:17px;line-height:13px;color:var(--white);letter-spacing:1.3px;transform:scaleX(1.5);transform-origin:left top;white-space:nowrap}

/* welcome */
.welcome-title{left:0;top:222px;width:1200px;text-align:center;font-size:11px;font-weight:700;color:var(--orange)}
.welcome-text{left:105px;top:245px;width:990px;text-align:center;padding:0 5px}

/* features */
.features{left:0;top:287px;width:1200px;height:170px;background:var(--band)}
.feature{top:300px;width:200px;text-align:center}
.feature-icon{width:58px;height:34px;margin:0 auto;border-radius:50%;background:var(--white);border:1px solid #d8d8d8;display:flex;align-items:center;justify-content:center}
.feature-kicker{margin-top:8px;font-size:11px;color:#a9a9a9;line-height:11px}
.feature-title{font-size:12px;font-weight:700;color:var(--heading);line-height:12px;letter-spacing:.5px}
.feature p{margin-top:3px;padding:0 5px;font-size:7.5px;line-height:9.6px}
.feature-btn{margin:5px auto 0;width:78px;height:12px;background:var(--white);font-size:6px;color:var(--orange);line-height:12px}

/* section titles */
.section-title{font-size:11px;font-weight:700;color:var(--orange);line-height:12px}
.section-rule{height:1px;background:#e4e4e4}
.section-rule::before{content:"";display:block;width:45px;height:2px;background:var(--orange);margin-top:-1px}
.pager{display:flex;gap:4px}
.pager span{width:22px;height:10px;background:var(--btn);display:flex;align-items:center;justify-content:center}

/* testimonials */
.quote{top:502px;width:267px;height:46px;background:#eee}
.quote-avatar{left:6px;top:3px;width:59px;height:24px;background:linear-gradient(180deg,#8a6a58,#4a3d3a)}
.quote p{left:75px;top:2px;width:185px;line-height:9.5px}
.quote-stars{left:6px;top:30px;display:flex;gap:2px}
.quote-mark{right:8px;top:27px;font-size:18px;color:#c9c9c9;font-weight:700}
.testimonial-text{left:105px;top:557px;width:560px}

/* skills */
.skill{left:689px;width:391px}
.skill-label{font-size:8px;font-weight:700;color:var(--heading);line-height:9px}
.skill-track{position:relative;height:8px;background:var(--track);border-radius:0 4px 4px 0;margin-top:1px}
.skill-fill{position:absolute;left:0;top:0;width:199px;height:8px}
.skill-value{position:absolute;left:8px;top:0;font-size:6px;line-height:8px;color:var(--heading)}

/* clients */
.clients{left:0;top:612px;width:1200px;height:101px;background:var(--band)}
.client{top:672px;width:100px;display:flex;align-items:center;gap:5px;justify-content:center}
.client i{width:12px;height:12px;border-radius:50%;background:var(--orange)}
.client span{font-size:15px;font-weight:700;color:var(--navy)}

/* responsive */
.rwd-text{left:105px;top:760px;width:638px}
.ticks{left:115px;top:802px;list-style:none}
.ticks li{font-size:8px;line-height:10.5px;display:flex;align-items:center;gap:8px}
.device{left:745px;top:750px;width:337px;height:86px;border-radius:4px;
  background:
    linear-gradient(180deg,rgba(255,255,255,0) 0%,rgba(255,255,255,0) 78%,#c9ccd1 80%,#eef0f2 100%),
    linear-gradient(135deg,var(--navy-deep) 0%,var(--navy) 45%,#2f4a8c 70%,var(--navy-deep) 100%);
  border:4px solid #b4b8bf;border-bottom:none}

/* footer */
.footer{left:0;top:870px;width:1200px;height:108px;background:var(--footer)}
.footer-col{top:889px;width:225px}
.footer-col h4{font-size:8px;font-weight:700;color:var(--white);letter-spacing:.5px;line-height:10px}
.footer-rule{height:1px;background:#3a3a3a;margin-top:4px}
.footer-rule::before{content:"";display:block;width:45px;height:2px;background:var(--orange);margin-top:-1px}
.footer-col ul{list-style:none;margin-top:8px}
.footer-col li{font-size:7px;color:var(--footer-text);line-height:10.8px}
.footer-col li::before{content:"›";color:var(--orange);margin-right:6px}
.tags{display:flex;flex-wrap:wrap;gap:3px 3px;margin-top:7px;width:222px}
.tags span{font-size:6px;color:#bbb;border:1px solid #444;background:#2f2f2f;padding:1px 6px;line-height:8px}
.base{left:0;top:978px;width:1200px;height:22px;background:var(--footer-base)}
.copyright{left:105px;top:985px;font-size:7px;color:var(--footer-text)}
.social-foot{left:858px;top:986px;display:flex;gap:21px}
.social-foot span{width:8px;height:8px;border-radius:50%;border:1px solid #888}
</style>
</head>
<body>

<div class="abs topline"></div>
<div class="abs brand"><span class="brand-dot"></span><span class="brand-name">Summit Path Advisory</span></div>
<div class="abs social-top"><span></span><span></span><span></span><span></span></div>
<div class="abs search"><svg width="10" height="10" viewBox="0 0 10 10"><circle cx="4" cy="4" r="3" fill="none" stroke="#f36f21" stroke-width="1.3"/><line x1="6.2" y1="6.2" x2="9" y2="9" stroke="#f36f21" stroke-width="1.5"/></svg></div>

<nav class="abs nav">
  <a>Home</a><a>Passion</a><a>Who We Are</a><a>Speaker</a><a>Free Videos</a><a>Web TV Show</a><a>Testimonials</a><a>Harlow Learning</a><a>Blog</a><a>Contact</a>
</nav>

<div class="abs hero" role="img" aria-label="Smiling coach in a dark blazer standing in a bright office"></div>
<svg class="abs hero-banner" viewBox="0 0 535 40" preserveAspectRatio="none"><polygon points="0,0 535,0 535,40 0,40 30,20" fill="#f36f21"/><polygon points="30,0 60,0 45,20 60,40 30,40 45,20" fill="#e35e12"/></svg>
<div class="abs hero-title">ALBUQUERQUE BUSINESS<br>COACHING AND CONSULTING</div>

<h2 class="abs welcome-title">Welcome To SummitPathAdvisory</h2>
<p class="abs welcome-text">Lorem ipsum dolor sit amet, consectetur adipiscing elit. Pellentesque imperdiet purus quis metus imperdiet fermentum. Suspendisse hendrerit id lacus id lobortis. Vestibulum quam elit, dapibus hendrerit id lacus id lobortis. Vestibulum quam elit, dapibus ac augue ut.</p>

<section class="abs features"></section>
<div class="abs feature" style="left:115px"><div class="feature-icon"><svg width="16" height="12"><ellipse cx="8" cy="6" rx="7" ry="4.5" fill="#f36f21" transform="rotate(-25 8 6)"/></svg></div><div class="feature-kicker">Summit Path Advisory</div><div class="feature-title">LOREM IPSUM</div><p>Lorem Ipsum is simply dummy text of the printing and typesetting industry. Lorem Ipsum has been the industry's standard dummy text ever since the 1500s, when an unknown printer took a galley of type and scrambled it to make a type specimen book.</p><div class="feature-btn">READ MORE</div></div>
<div class="abs feature" style="left:366px"><div class="feature-icon"><svg width="14" height="14"><circle cx="7" cy="7" r="6" fill="#f36f21"/><circle cx="7" cy="7" r="2.5" fill="#fff"/></svg></div><div class="feature-kicker">Summit Path Advisory</div><div class="feature-title">LOREM IPSUM</div><p>Lorem Ipsum is simply dummy text of the printing and typesetting industry. Lorem Ipsum has been the industry's standard dummy text ever since the 1500s, when an unknown printer took a galley of type and scrambled it to make a type specimen book.</p><div class="feature-btn">READ MORE</div></div>
<div class="abs feature" style="left:617px"><div class="feature-icon"><svg width="14" height="14"><rect x="2" y="4" width="10" height="9" fill="#f36f21"/><circle cx="7" cy="4" r="2.5" fill="#f36f21"/></svg></div><div class="feature-kicker">Summit Path Advisory</div><div class="feature-title">LOREM IPSUM</div><p>Lorem Ipsum is simply dummy text of the printing and typesetting industry. Lorem Ipsum has been the industry's standard dummy text ever since the 1500s, when an unknown printer took a galley of type and scrambled it to make a type specimen book.</p><div class="feature-btn">READ MORE</div></div>
<div class="abs feature" style="left:867px"><div class="feature-icon"><svg width="14" height="14"><rect x="1" y="2" width="9" height="5" fill="#f36f21" transform="rotate(-35 5 5)"/><line x1="7" y1="7" x2="12" y2="13" stroke="#f36f21" stroke-width="2"/></svg></div><div class="feature-kicker">Summit Path Advisory</div><div class="feature-title">LOREM IPSUM</div><p>Lorem Ipsum is simply dummy text of the printing and typesetting industry. Lorem Ipsum has been the industry's standard dummy text ever since the 1500s, when an unknown printer took a galley of type and scrambled it to make a type specimen book.</p><div class="feature-btn">READ MORE</div></div>

<h3 class="abs section-title" style="left:105px;top:477px">What They Said About Us</h3>
<div class="abs section-rule" style="left:105px;top:493px;width:560px"></div>
<div class="abs pager" style="left:613px;top:481px"><span><svg width="5" height="5"><polygon points="4,0 4,5 0,2.5" fill="#fff"/></svg></span><span><svg width="5" height="5"><polygon points="1,0 1,5 5,2.5" fill="#fff"/></svg></span></div>

<div class="abs quote" style="left:105px">
  <div class="abs quote-avatar" role="img" aria-label="Client portrait"></div>
  <p class="abs">Lorem ipsum dolor sit amet, consectetur adipiscing elit pellentesque,Lorem ipsum dolor sit amet, consectetur.</p>
  <div class="abs quote-stars"><svg width="60" height="8"><g fill="#f5b50a"><polygon points="4,0 5,3 8,3 5.5,5 6.5,8 4,6 1.5,8 2.5,5 0,3 3,3"/><polygon transform="translate(12)" points="4,0 5,3 8,3 5.5,5 6.5,8 4,6 1.5,8 2.5,5 0,3 3,3"/><polygon transform="translate(24)" points="4,0 5,3 8,3 5.5,5 6.5,8 4,6 1.5,8 2.5,5 0,3 3,3"/><polygon transform="translate(36)" points="4,0 5,3 8,3 5.5,5 6.5,8 4,6 1.5,8 2.5,5 0,3 3,3"/><polygon transform="translate(48)" points="4,0 5,3 8,3 5.5,5 6.5,8 4,6 1.5,8 2.5,5 0,3 3,3"/></g></svg></div>
  <span class="abs quote-mark">”</span>
</div>
<div class="abs quote" style="left:398px">
  <div class="abs quote-avatar" role="img" aria-label="Client portrait"></div>
  <p class="abs">Lorem ipsum dolor sit amet, consectetur adipiscing elit pellentesque,Lorem ipsum dolor sit amet, consectetur.</p>
  <div class="abs quote-stars"><svg width="60" height="8"><g fill="#f5b50a"><polygon points="4,0 5,3 8,3 5.5,5 6.5,8 4,6 1.5,8 2.5,5 0,3 3,3"/><polygon transform="translate(12)" points="4,0 5,3 8,3 5.5,5 6.5,8 4,6 1.5,8 2.5,5 0,3 3,3"/><polygon transform="translate(24)" points="4,0 5,3 8,3 5.5,5 6.5,8 4,6 1.5,8 2.5,5 0,3 3,3"/><polygon transform="translate(36)" points="4,0 5,3 8,3 5.5,5 6.5,8 4,6 1.5,8 2.5,5 0,3 3,3"/><polygon transform="translate(48)" points="4,0 5,3 8,3 5.5,5 6.5,8 4,6 1.5,8 2.5,5 0,3 3,3"/></g></svg></div>
  <span class="abs quote-mark">”</span>
</div>
<p class="abs testimonial-text">Lorem ipsum dolor sit amet, consectetur adipiscing elit. Pellentesque imperdiet purus quis metus imperdiet fermentum. Suspendisse hendrerit id lacus id lobortis. Vestibulum quam elit, dapibus ac augue ut, porttitor viverra dui. Pellentesque imperdiet purus quis metus imperdiet fermentum. Suspendisse hendrerit id lacus id lobortis. Vestibulum quam elit, apibus ac augue ut, porttitor viverra dui. Lorem ipsum dolor sit.</p>

<h3 class="abs section-title" style="left:689px;top:477px">Our Skills</h3>
<div class="abs section-rule" style="left:689px;top:493px;width:391px"></div>
<div class="abs skill" style="top:500px"><div class="skill-label">Lorem Ipsum</div><div class="skill-track"><svg class="skill-fill" viewBox="0 0 199 8"><polygon points="0,0 192,0 199,4 192,8 0,8" fill="#f36f21"/><rect width="44" height="8" fill="#e4e4e4"/></svg><span class="skill-value">50</span></div></div>
<div class="abs skill" style="top:523px"><div class="skill-label">Lorem Ipsum</div><div class="skill-track"><svg class="skill-fill" viewBox="0 0 199 8"><polygon points="0,0 192,0 199,4 192,8 0,8" fill="#f36f21"/><rect width="44" height="8" fill="#e4e4e4"/></svg><span class="skill-value">50%</span></div></div>
<div class="abs skill" style="top:547px"><div class="skill-label">Lorem Ipsum</div><div class="skill-track"><svg class="skill-fill" viewBox="0 0 199 8"><polygon points="0,0 192,0 199,4 192,8 0,8" fill="#f36f21"/><rect width="44" height="8" fill="#e4e4e4"/></svg><span class="skill-value">50%</span></div></div>
<div class="abs skill" style="top:570px"><div class="skill-label">Lorem Ipsum</div><div class="skill-track"><svg class="skill-fill" viewBox="0 0 199 8"><polygon points="0,0 192,0 199,4 192,8 0,8" fill="#f36f21"/><rect width="44" height="8" fill="#e4e4e4"/></svg><span class="skill-value">50%</span></div></div>

<section class="abs clients"></section>
<h3 class="abs section-title" style="left:105px;top:636px">Our Clients</h3>
<div class="abs section-rule" style="left:105px;top:652px;width:100px;background:none"></div>
<div class="abs pager" style="left:1030px;top:638px"><span><svg width="5" height="5"><polygon points="4,0 4,5 0,2.5" fill="#fff"/></svg></span><span><svg width="5" height="5"><polygon points="1,0 1,5 5,2.5" fill="#fff"/></svg></span></div>
<div class="abs client" style="left:98px"><i></i><span>Vireo</span></div>
<div class="abs client" style="left:245px"><i></i><span>Orbix</span></div>
<div class="abs client" style="left:395px"><i></i><span>Boxline</span></div>
<div class="abs client" style="left:542px"><i></i><span>Vireo</span></div>
<div class="abs client" style="left:688px"><i></i><span>Orbix</span></div>
<div class="abs client" style="left:837px"><i></i><span>Boxline</span></div>
<div class="abs client" style="left:985px"><i></i><span>Vireo</span></div>

<h3 class="abs section-title" style="left:105px;top:737px">Responsive Web Design</h3>
<div class="abs section-rule" style="left:105px;top:753px;width:645px"></div>
<p class="abs rwd-text">Lorem ipsum dolor sit amet, consectetur adipiscing elit. Pellentesque imperdiet purus quis metus imperdiet fermentum. Suspendisse hendrerit id lacus id lobortis. Vestibulum quam elit, dapibus ac augue ut, porttitor viverra dui. Pellentesque imperdiet purus quis metus imperdiet fermentum. Suspendisse hendrerit id lacus id lobortis. Vestibulum quam elit, apibus ac augue ut, porttitor viverra dui. Lorem ipsum dolor sit amet, consectet urapibus ac augue ut, porttitor viverra dui. Lorem ipsum dolor sit amet, consectetur adipiscing elit.</p>
<ul class="abs ticks">
  <li><svg width="9" height="7"><polyline points="1,3.5 3.5,6 8,1" fill="none" stroke="#f36f21" stroke-width="1.6"/></svg>Lorem ipsum dolor sit amet, consectetur adipiscing elit pellentesque</li>
  <li><svg width="9" height="7"><polyline points="1,3.5 3.5,6 8,1" fill="none" stroke="#f36f21" stroke-width="1.6"/></svg>Lorem ipsum dolor sit amet, consectetur adipiscing elit pellentesque</li>
  <li><svg width="9" height="7"><polyline points="1,3.5 3.5,6 8,1" fill="none" stroke="#f36f21" stroke-width="1.6"/></svg>Lorem ipsum dolor sit amet, consectetur adipiscing elit pellentesque</li>
  <li><svg width="9" height="7"><polyline points="1,3.5 3.5,6 8,1" fill="none" stroke="#f36f21" stroke-width="1.6"/></svg>Lorem ipsum dolor sit amet, consectetur adipiscing elit pellentesque</li>
</ul>
<div class="abs device" role="img" aria-label="Laptop with a dark blue screen showing app tiles"></div>

<footer class="abs footer"></footer>
<div class="abs footer-col" style="left:105px"><h4>MAIN MENU</h4><div class="footer-rule"></div><ul><li>Home Page</li><li>About Us</li><li>Our Blog</li><li>Our Portfolio</li><li>FAQ</li></ul></div>
<div class="abs footer-col" style="left:357px"><h4>OUR FRIENDS</h4><div class="footer-rule"></div><ul><li>adipiscing elit integer</li><li>magna euismod</li><li>purus molestie</li><li>adipiscing elit integer</li><li>purus molestie</li></ul></div>
<div class="abs footer-col" style="left:608px"><h4>USEFUL LINKS</h4><div class="footer-rule"></div><ul><li>Privacy policy</li><li>Terms of use</li><li>purus molestie</li><li>adipiscing elit integer</li><li>magna euismod</li></ul></div>
<div class="abs footer-col" style="left:858px"><h4>TAG CLOUD</h4><div class="footer-rule"></div><div class="tags"><span>Design</span><span>User Interface</span><span>Performance</span><span>Development</span><span>PressKit</span><span>SEO</span><span>SiteForge</span><span>NetStack</span><span>TeamShare</span><span>GridKit</span></div></div>

<div class="abs base"></div>
<div class="abs copyright">© copyright 2014. All right reserved.</div>
<div class="abs social-foot"><span></span><span></span><span></span><span></span><span></span><span></span><span></span><span></span></div>

</body>
</html>
```